Layout for site fence advertising - length approx. 250 cm x 125 cm

The advertising will later be printed on a PVC film and used for events or on sports fields.

Main services :
Your regional contact at
Real estate and business financing
independent insurance advice

```html
<!DOCTYPE html>
<html lang="en">
<head>
<meta charset="utf-8">
<title>Brenner Vermögensberatung – Site Fence Banner</title>
<link href="https://fonts.googleapis.com/css2?family=Comfortaa:wght@700&display=swap" rel="stylesheet">
<style>
  :root {
    --page-bg: #f2f3f7;
    --brand-blue: #2a56a8;
    --brand-navy: #1f3f80;
    --headline-blue: #2a4fa3;
    --headline-grey: #4f5153;
    --edge-grey: #55595e;
    --phone-bg: #6b6e72;
    --white: #ffffff;
  }
  html, body {
    margin: 0;
    padding: 0;
    width: 1050px;
    height: 1200px;
    overflow: hidden;
    background: var(--page-bg);
  }
  .banner {
    position: absolute;
    left: 35px;
    top: 355px;
    width: 980px;
    height: 490px;
    box-shadow: 0 6px 16px rgba(0,0,0,0.25);
    overflow: hidden;
    font-family: "Comfortaa", sans-serif;
  }
  .banner-art {
    position: absolute;
    inset: 0;
    width: 980px;
    height: 490px;
  }
  .headline {
    position: absolute;
    left: 20px;
    top: 30px;
    width: 400px;
    margin: 0;
    text-align: center;
    font-weight: 700;
    font-size: 28px;
    line-height: 45px;
    color: var(--headline-grey);
    text-shadow: 0 0 3px var(--white), 0 0 6px var(--white);
  }
  .headline .accent { color: var(--headline-blue); }
  .brand {
    position: absolute;
    left: 58px;
    top: 311px;
    display: flex;
    align-items: center;
  }
  .brand-mark {
    width: 118px;
    height: 118px;
    border: 3px solid var(--white);
    border-radius: 50%;
    box-sizing: border-box;
    flex: none;
  }
  .brand-divider {
    width: 3px;
    height: 122px;
    background: var(--white);
    margin: 0 9px 0 11px;
    flex: none;
  }
  .brand-text {
    color: var(--white);
    font-weight: 700;
    white-space: nowrap;
  }
  .brand-name { font-size: 19px; margin: 0 0 6px; }
  .brand-name small { font-size: 15px; }
  .brand-tagline { font-size: 15px; margin: 0; }
  .phone {
    position: absolute;
    left: 268px;
    top: 423px;
    width: 322px;
    height: 40px;
    background: linear-gradient(90deg, var(--phone-bg) 75%, rgba(107,110,114,0.4));
    color: var(--white);
    font-weight: 700;
    font-size: 31px;
    line-height: 42px;
    padding-left: 10px;
    box-sizing: border-box;
    letter-spacing: 0.5px;
    white-space: nowrap;
  }
  .portrait {
    position: absolute;
    left: 592px;
    top: 303px;
    width: 138px;
    height: 174px;
    border: 4px solid var(--white);
    border-radius: 10px;
    box-sizing: border-box;
    background: linear-gradient(180deg, #5a4636 0%, #9a8d85 45%, #2b2e36 100%);
  }
</style>
</head>
<body>
  <section class="banner">
    <svg class="banner-art" viewBox="0 0 980 490" xmlns="http://www.w3.org/2000/svg">
      <defs>
        <radialGradient id="panelGradient" cx="0.35" cy="0.35" r="0.7">
          <stop offset="0" stop-color="#f7f8f9"/>
          <stop offset="1" stop-color="#d6d9dc"/>
        </radialGradient>
        <linearGradient id="sceneGradient" x1="0" y1="0" x2="0" y2="1">
          <stop offset="0" stop-color="#c9d3dc"/>
          <stop offset="0.35" stop-color="#c8a57e"/>
          <stop offset="0.7" stop-color="#6f9a4a"/>
          <stop offset="1" stop-color="#b8b6b1"/>
        </linearGradient>
      </defs>
      <rect class="panel-light" width="980" height="490" fill="url(#panelGradient)"/>
      <path class="blue-band" d="M0 230 C140 290 380 300 620 255 L980 255 L980 490 L0 490 Z" fill="var(--brand-blue)"/>
      <path class="blue-band-shade" d="M0 230 C140 290 380 300 620 255 L620 265 C380 312 140 302 0 245 Z" fill="var(--brand-navy)" opacity="0.6"/>
      <path class="photo-edge" d="M384 0 C470 140 560 290 660 370 C740 430 820 470 900 490 L980 490 L980 0 Z" fill="var(--edge-grey)"/>
      <path class="bottom-wave" d="M640 370 C730 440 820 480 880 490 L700 490 Z" fill="var(--brand-navy)"/>
      <path class="house-photo" role="img" aria-label="Photo of a brick family house with green lawn and driveway"
        d="M396 0 C480 140 570 290 670 368 C750 428 830 468 905 490 L980 490 L980 0 Z" fill="url(#sceneGradient)"/>
    </svg>

    <h1 class="headline">
      <span class="accent">Your regional contact</span><br>
      <span class="accent">at</span> REAL ESTATE <span class="accent">and</span><br>
      BUSINESS FINANCING<br>
      <span class="accent">independent</span> INSURANCE<br>
      ADVICE
    </h1>

    <div class="brand">
      <div class="brand-mark"></div>
      <div class="brand-divider"></div>
      <div class="brand-text">
        <p class="brand-name">Brenner Vermögensberatung <small>GmbH</small></p>
        <p class="brand-tagline">Finanzieren, Versichern, Vorsorgen</p>
      </div>
    </div>

    <div class="phone">+43 660 214 5807</div>

    <div class="portrait" role="img" aria-label="Portrait photo of the advisor"></div>
  </section>
</body>
</html>
```